Business Card Design

We are a residential half way house for the addict ,the alcoholic and dual diagnosed in recovery.
i house both men and woman age 18+

Industry/Entity Type

Residential

```html
<!DOCTYPE html>
<html lang="en">
<head>
<meta charset="utf-8">
<title>Marigold Family Sober House Inc. – Business Card</title>
<link rel="stylesheet" href="https://fonts.googleapis.com/css2?family=Questrial&family=Tinos:ital,wght@0,400;0,700;1,700&family=Arimo:wght@700&display=swap">
<style>
  :root {
    --green: #1e8500;
    --black: #000000;
    --header-top: #8e9696;
    --stripe: #cdd6d6;
    --panel: #a9b9b8;
    --panel-edge: #1a1a1a;
    --white: #ffffff;
    --navy: #0d1466;
    --red: #d60000;
    --ink: #1a1a1a;
  }
  html, body {
    margin: 0;
    padding: 0;
    overflow: hidden;
    background: #ffffff;
  }
  .card {
    position: relative;
    width: 1200px;
    height: 780px;
    background: var(--green);
    overflow: hidden;
  }
  .header {
    position: absolute;
    left: 0; top: 0;
    width: 1200px; height: 126px;
    background: linear-gradient(to bottom, var(--header-top) 0%, #2a2d2d 40%, var(--black) 70%, var(--black) 100%);
  }
  .company-name {
    position: absolute;
    left: 20px; top: 20px;
    margin: 0;
    font-family: "Questrial", sans-serif;
    font-weight: 400;
    font-size: 63px;
    line-height: 1;
    color: var(--white);
    letter-spacing: 0.5px;
    white-space: nowrap;
  }
  .address-stripe {
    position: absolute;
    left: 0; top: 124px;
    width: 1200px; height: 26px;
    background: linear-gradient(to bottom, #e3eaea, var(--stripe));
  }
  .address {
    position: absolute;
    left: 21px; top: 1px;
    font-family: "Tinos", serif;
    font-size: 24px;
    line-height: 1;
    color: var(--ink);
    white-space: nowrap;
  }
  .header-fade {
    position: absolute;
    left: 0; top: 150px;
    width: 1200px; height: 50px;
    background: linear-gradient(to bottom, var(--black) 0%, #555 45%, #dcdcdc 80%, var(--white) 100%);
  }
  .banner {
    position: absolute;
    left: 0; top: 332px;
    width: 1200px; height: 182px;
    background: var(--panel);
    border-top: 7px solid var(--panel-edge);
    border-bottom: 4px solid #3a3f3f;
    box-sizing: border-box;
    box-shadow: inset 0 0 0 2px #2b2f2f;
  }
  .tagline {
    position: absolute;
    left: 20px; top: 25px;
    margin: 0;
    font-family: "Tinos", serif;
    font-style: italic;
    font-weight: 700;
    font-size: 44px;
    line-height: 66px;
    color: var(--navy);
  }
  .tagline .second {
    display: block;
    padding-left: 88px;
  }
  .owner {
    position: absolute;
    right: 38px; top: 28px;
    text-align: right;
    color: var(--red);
    font-family: "Tinos", serif;
    font-weight: 700;
  }
  .owner-name {
    margin: 0;
    font-size: 64px;
    line-height: 1;
  }
  .owner-role {
    margin: 6px 0 0;
    font-size: 24px;
    line-height: 1;
  }
  .contact {
    position: absolute;
    left: 48px; top: 716px;
    margin: 0;
    font-family: "Arimo", sans-serif;
    font-weight: 700;
    font-size: 22px;
    color: var(--white);
    white-space: nowrap;
    display: flex;
    align-items: center;
    gap: 8px;
  }
  .contact .sep {
    font-size: 16px;
    margin: 0 4px;
  }
</style>
</head>
<body>
  <div class="card">
    <div class="header">
      <h1 class="company-name">Marigold Family Sober House Inc.</h1>
    </div>
    <div class="address-stripe">
      <span class="address">4127 Palmetto Rd. Lake Harbor, Fla 33400</span>
    </div>
    <div class="header-fade"></div>

    <div class="banner">
      <p class="tagline">
        <span class="first">&#8221;Providing a</span>
        <span class="second">Meaningful Recovery&#8221;</span>
      </p>
      <div class="owner">
        <p class="owner-name">Renata Alvarez</p>
        <p class="owner-role">Owner (15 yrs. in recovery)</p>
      </div>
    </div>

    <p class="contact">
      <span>(555) 014-0305</span>
      <span class="sep">&#10035;</span>
      <span>(555) 014-0306</span>
      <span class="sep">&#10035;</span>
      <span>Fax: (555) 014-5536</span>
      <span class="sep">&#10035;</span>
      <span>Email: renataalvarez@example.com</span>
    </p>
  </div>
</body>
</html>
```